Laundry Store front design

I own a laundry business and require a design for the shop front.

I have uploaded 3 photos with window numbers on, 1 thru 5. It might be better to stich these together as I want the design to flow across 1-5 but only the top of 3.

I have uploaded some pdf documents with more details.

Font styles to use
Serif

Colors
0054AA
0677BA
7BADD7
CADEEF
E8F1F8

```html
<!DOCTYPE html>
<html lang="en">
<head>
<meta charset="utf-8">
<title>Bluewave Laundry Services – Shop Front Windows</title>
<link href="https://fonts.googleapis.com/css2?family=Source+Sans+3:wght@400;600;700&display=swap" rel="stylesheet">
<style>
  :root {
    --navy: #0054AA;
    --blue: #0677BA;
    --sky: #7BADD7;
    --pale: #CADEEF;
    --mist: #E8F1F8;
    --frame: #6a5a47;
    --red: #e3262a;
    --green: #3a9a3c;
    --ink: #1a1a1a;
    --page: #ffffff;
  }
  * { margin: 0; padding: 0; box-sizing: border-box; }
  html, body { width: 1200px; height: 482px; overflow: hidden; background: var(--page); }
  body { font-family: "Source Sans 3", sans-serif; position: relative; }

  .window-group { position: absolute; top: 150px; height: 176px; background: var(--frame); }
  .pane { position: absolute; background: var(--pale); overflow: hidden; }
  .pane.plain { background: var(--pale); }
  .pane.pattern { background: radial-gradient(circle at 40% 40%, var(--mist), var(--pale)); }
  .pane.photo { background: linear-gradient(135deg, #dfe6ec 0%, #b9c6d2 45%, #8fa3b5 100%); }

  .brand-name { position: absolute; inset: 0; display: flex; align-items: center; justify-content: center;
    color: var(--blue); font-weight: 600; line-height: 1; text-align: center; }

  .service-list { list-style: none; color: var(--blue); }
  .service-list li { position: relative; padding-left: 13px; }
  .service-list li::before { content: ""; position: absolute; left: 0; top: 0.35em;
    border-left: 8px solid var(--blue); border-top: 4px solid transparent; border-bottom: 4px solid transparent; }
  .service-list.small li { padding-left: 8px; }
  .service-list.small li::before { border-left-width: 5px; border-top-width: 3px; border-bottom-width: 3px; top: 0.3em; }
  .service-list.dark { color: var(--ink); }
  .service-list.dark li::before { border-left-color: var(--navy); }

  .offer-title { color: var(--red); font-size: 11px; line-height: 11px; text-align: center; }
  .promo-text { color: var(--blue); font-size: 8.5px; line-height: 9.5px; text-align: center; }
  .discount { color: var(--red); text-align: center; font-weight: 700; }
  .photo-caption { position: absolute; color: #fff; font-weight: 600; font-size: 8px; line-height: 8.5px; }
  .web-address { position: absolute; right: 4px; bottom: 3px; color: var(--navy); font-size: 4px; }

  .price-badge { position: absolute; top: 101px; width: 71px; height: 71px; background: var(--navy);
    border-radius: 36px 36px 0 0; color: #fff; text-align: center; display: flex; flex-direction: column;
    justify-content: center; padding-top: 8px; font-size: 9.5px; line-height: 11px; }
  .price-badge small { font-size: 6px; line-height: 10px; }
</style>
</head>
<body>

<!-- Window 1 -->
<section class="window-group" style="left:20px;width:179px;">
  <div class="pane photo" style="left:2px;top:2px;width:108px;height:172px;" role="img" aria-label="Photo of a woman loading laundry into a washing machine, framed by blue arcs">
    <svg width="108" height="172" viewBox="0 0 108 172">
      <circle cx="30" cy="75" r="74" fill="none" stroke="var(--navy)" stroke-width="5"/>
      <circle cx="30" cy="75" r="82" fill="none" stroke="var(--sky)" stroke-width="6"/>
    </svg>
  </div>
  <div class="pane plain" style="left:113px;top:2px;width:64px;height:40px;">
    <span class="brand-name" style="font-size:11px;">bluewave</span>
  </div>
  <div class="pane plain" style="left:113px;top:45px;width:64px;height:50px;padding:6px 4px;">
    <p class="offer-title">Special<br>Price for</p>
    <ul class="service-list small dark" style="font-size:6.5px;line-height:9px;margin-top:3px;">
      <li>Property<br>Managers</li>
    </ul>
  </div>
  <div class="pane plain" style="left:113px;top:98px;width:64px;height:76px;padding:6px 3px;">
    <ul class="service-list small dark" style="font-size:6.3px;line-height:9.2px;">
      <li>Hotels,</li><li>Apartments</li><li>Villas</li><li>Restaurants<br>&amp; More</li>
    </ul>
  </div>
</section>

<!-- Window 2 -->
<section class="window-group" style="left:218px;width:172px;">
  <div class="pane plain" style="left:2px;top:2px;width:42px;height:42px;">
    <span class="brand-name" style="font-size:8px;">bluewave</span>
  </div>
  <div class="pane plain" style="left:2px;top:47px;width:42px;height:50px;padding-top:4px;">
    <p class="promo-text">Book<br>Online<br>Through<br>Our App<br>&amp; Get</p>
  </div>
  <div class="pane plain" style="left:2px;top:100px;width:42px;height:74px;padding-top:4px;">
    <p class="discount" style="font-size:16px;line-height:16px;">20%</p>
    <p class="discount" style="font-size:7.5px;line-height:8px;">Discount</p>
    <p class="promo-text" style="font-size:6px;line-height:8px;color:var(--navy);">on First order</p>
  </div>
  <div class="pane photo" style="left:47px;top:2px;width:123px;height:172px;" role="img" aria-label="Photo of a woman looking into a front-loading washing machine">
    <p class="photo-caption" style="left:8px;top:92px;">Free<br>delivery<br>within<br>local area</p>
    <p class="web-address">www.bluewavelaundry.example</p>
  </div>
</section>

<!-- Window 3 -->
<section class="window-group" style="left:434px;width:226px;">
  <div class="pane pattern" style="left:2px;top:2px;width:67px;height:42px;" role="img" aria-label="Bubble pattern"></div>
  <div class="pane plain" style="left:72px;top:2px;width:82px;height:42px;">
    <span class="brand-name" style="font-size:17px;">bluewave</span>
  </div>
  <div class="pane pattern" style="left:157px;top:2px;width:67px;height:42px;" role="img" aria-label="Bubble pattern"></div>
  <div class="pane pattern" style="left:2px;top:48px;width:64px;height:59px;" role="img" aria-label="Bubble pattern"></div>
  <div class="pane pattern" style="left:2px;top:110px;width:64px;height:64px;" role="img" aria-label="Bubble pattern"></div>
  <div class="pane plain" style="left:70px;top:48px;width:78px;height:126px;padding:12px 0 0 4px;">
    <ul class="service-list" style="font-size:11.5px;line-height:13px;">
      <li>Service<br>Washes</li><li>Ironing<br>Service</li><li>Duvets</li><li>Linen</li><li>Towels</li>
    </ul>
  </div>
  <div class="pane plain" style="left:151px;top:48px;width:73px;height:126px;padding:18px 0 0 2px;">
    <ul class="service-list" style="font-size:11.5px;line-height:13px;">
      <li>Wedding<br>Dresses,</li><li>Upholstery</li><li>Rugs</li><li>Collection<br>&amp; Delivery</li>
    </ul>
  </div>
</section>

<!-- Window 4 -->
<section class="window-group" style="left:713px;width:223px;">
  <div class="pane plain" style="left:2px;top:2px;width:60px;height:42px;">
    <svg width="60" height="42" viewBox="0 0 60 42" aria-hidden="true"><circle cx="30" cy="21" r="11" fill="var(--green)"/></svg>
  </div>
  <div class="pane plain" style="left:65px;top:2px;width:78px;height:42px;">
    <span class="brand-name" style="font-size:14px;">PureRinse</span>
  </div>
  <div class="pane pattern" style="left:146px;top:2px;width:75px;height:42px;" role="img" aria-label="Bubble pattern"></div>
  <div class="pane pattern" style="left:2px;top:48px;width:58px;height:59px;" role="img" aria-label="Bubble pattern"></div>
  <div class="pane pattern" style="left:2px;top:110px;width:58px;height:64px;" role="img" aria-label="Bubble pattern"></div>
  <div class="pane plain" style="left:63px;top:48px;width:76px;height:126px;padding:3px 0 0 2px;">
    <ul class="service-list small" style="font-size:8.6px;line-height:10.2px;">
      <li>Specially<br>adapted<br>machines</li><li>Eco-friendly<br>no harsh<br>chemicals</li><li>VIP 2 hour<br>service<br>available</li><li>Superior<br>stain removal</li>
    </ul>
  </div>
  <div class="pane plain" style="left:142px;top:48px;width:79px;height:126px;">
    <p style="position:absolute;left:0;right:0;top:30px;text-align:center;color:var(--blue);font-weight:600;font-size:14px;line-height:14px;">PureRinse</p>
    <p style="position:absolute;left:0;right:0;top:46px;text-align:center;color:var(--blue);font-size:6px;letter-spacing:1.5px;">WET CLEANING</p>
    <svg style="position:absolute;left:30px;top:57px;" width="20" height="7" viewBox="0 0 20 7" aria-hidden="true"><rect width="20" height="7" rx="3.5" fill="var(--navy)"/></svg>
    <ul class="service-list small" style="position:absolute;left:2px;top:83px;font-size:8.6px;line-height:10.2px;">
      <li>Suitable for all<br>‘dry clean only’<br>garments</li>
    </ul>
  </div>
</section>

<!-- Window 5 -->
<section class="window-group" style="left:958px;width:211px;">
  <div class="pane plain" style="left:2px;top:2px;width:52px;height:42px;">
    <span class="brand-name" style="font-size:10px;">bluewave</span>
  </div>
  <div class="pane pattern" style="left:2px;top:48px;width:52px;height:59px;" role="img" aria-label="Bubble pattern"></div>
  <div class="pane pattern" style="left:2px;top:110px;width:52px;height:64px;" role="img" aria-label="Bubble pattern"></div>
  <div class="pane photo" style="left:57px;top:2px;width:152px;height:172px;" role="img" aria-label="Photo of a woman holding laundry in front of washing machines">
    <div class="price-badge" style="left:7px;">Wash,<br>Dry<br>&amp; Fold<br>service</div>
    <div class="price-badge" style="left:80px;">starting at<br>2 euros<br>per KG<small>Same Day Service</small></div>
  </div>
</section>

</body>
</html>
```